Brindle Advisory Business Card Design

Business card for business consulting company, using attached logo. We do financial and strategic consulting, and want a clean, professional image with a bit of fun. Our logo is a flat whale tail, which symbolizes the Orca whale, a highly collaborative, group based animal that is very successful in navigating the ocean, protecting the herd, and hunting. We like the logo that is blue and gray on white one one side, but would be open to a blue card with white lettering on the other side... or whatever you'd suggest
Updates
Hi all - I have had the logo modified to take the shadowing off the tail. I will post it on the brief... under a file name called updated logo. thank you Added Saturday, April 25, 2015
Target Market(s)
Small to medium sized businesses ($10M to $500M in revenue per year), financial and sales executives, general managers, attorneys and CPAs
Industry/Entity Type
Financial
Contact Information for Business Card
Want company name, contact info - name, title, telephone, email, website, linkedin, twitter and Facebook. No physical address yet.
Requirements
Must have
- contemporary design, bold, strong, confident but with a bit of fun. prominently feature the logo and the whale tail icon
Nice to have
- unique touches that would differentiate us from a regular card... for example, logo and writing all on front on white background, but on back - logo in white on a blue background
- open to idea of different shapes of card than standard... but not sure
Should not have
- ?

```html
<!DOCTYPE html>
<html lang="en">
<head>
<meta charset="utf-8">
<title>Brindle Advisory — Business Card</title>
<link href="https://fonts.googleapis.com/css2?family=Open+Sans:wght@300;400;600;700&display=swap" rel="stylesheet">
<style>
  :root {
    --navy: #0b3d73;
    --navy-soft: #12467f;
    --white: #ffffff;
    --grey: #8d8f93;
    --ink: #1f3f6b;
    --stage: #e8e9eb;
    --divider: rgba(255,255,255,0.45);
  }
  * { margin: 0; padding: 0; box-sizing: border-box; }
  html, body { width: 1200px; height: 873px; overflow: hidden; }
  body {
    background: var(--stage);
    font-family: "Open Sans", Arial, sans-serif;
    position: relative;
  }
  .card {
    position: absolute;
    top: 285px;
    width: 530px;
    height: 303px;
    border-radius: 4px;
    box-shadow: 0 6px 18px rgba(0,0,0,0.18);
    overflow: hidden;
  }
  .card--front { left: 45px; background: var(--white); }
  .card--back  { left: 625px; background: var(--navy); }

  /* wordmark */
  .brand { position: absolute; display: flex; align-items: center; }
  .brand__mark { width: 30px; height: 30px; border-radius: 5px; margin-right: 8px; }
  .brand__name { font-weight: 400; font-size: 34px; letter-spacing: -1px; line-height: 1; }
  .brand__tagline {
    position: absolute; font-weight: 300; font-size: 11px; letter-spacing: 0.3px;
  }

  .card--front .brand { left: 196px; top: 30px; }
  .card--front .brand__mark { background: var(--navy); }
  .card--front .brand__name { color: var(--grey); }
  .card--front .brand__tagline { left: 396px; top: 72px; color: var(--grey); }

  /* blue band */
  .band {
    position: absolute; left: 0; right: 0; top: 108px; height: 92px;
    background: var(--navy); color: var(--white);
  }
  .person { position: absolute; left: 40px; top: 22px; text-align: right; width: 170px; }
  .person__name { font-weight: 700; font-size: 14px; letter-spacing: 0.5px; }
  .person__title { font-weight: 400; font-size: 13px; margin-top: 2px; }
  .band__divider {
    position: absolute; left: 226px; top: 14px; width: 1px; height: 64px; background: var(--divider);
  }
  .contacts { position: absolute; left: 244px; top: 14px; list-style: none; }
  .contacts li { display: flex; align-items: center; font-size: 13px; height: 21px; }
  .contacts svg { width: 13px; height: 13px; margin-right: 8px; }

  .social { position: absolute; left: 40px; top: 222px; display: flex; gap: 5px; }
  .social span { width: 14px; height: 14px; border-radius: 2px; background: var(--navy); }
  .address {
    position: absolute; left: 40px; top: 246px; font-size: 12px; color: var(--ink);
  }

  /* back */
  .card--back .brand { left: 150px; top: 108px; }
  .card--back .brand__mark { background: var(--white); }
  .card--back .brand__name { color: var(--white); }
  .card--back .brand__tagline { left: 290px; top: 150px; color: var(--white); }
  .website {
    position: absolute; left: 34px; bottom: 30px; color: var(--white);
    font-size: 10px; letter-spacing: 3px; font-weight: 400;
  }
</style>
</head>
<body>
  <section class="card card--front" aria-label="Card front">
    <div class="brand">
      <span class="brand__mark"></span>
      <span class="brand__name">Brindle Advisory</span>
    </div>
    <span class="brand__tagline">business consulting</span>

    <div class="band">
      <div class="person">
        <p class="person__name">DANA WHITFIELD</p>
        <p class="person__title">Manager</p>
      </div>
      <span class="band__divider"></span>
      <ul class="contacts">
        <li>
          <svg viewBox="0 0 13 13"><rect width="13" height="13" rx="2" fill="#fff"/><path d="M4 3.2l1.4 1.6-.8 1a5 5 0 0 0 2.6 2.6l1-.8 1.6 1.4-.8 1.2C6.5 10 3 6.5 2.8 4z" fill="#0b3d73"/></svg>
          5550142873
        </li>
        <li>
          <svg viewBox="0 0 13 13"><rect width="13" height="13" rx="2" fill="#fff"/><rect x="4.3" y="2.5" width="4.4" height="8" rx="0.8" fill="#0b3d73"/><rect x="5" y="3.4" width="3" height="5" fill="#fff"/></svg>
          5550142873
        </li>
        <li>
          <svg viewBox="0 0 13 13"><rect width="13" height="13" rx="2" fill="#fff"/><rect x="2.5" y="4" width="8" height="5.5" fill="#0b3d73"/><path d="M2.5 4l4 3 4-3" stroke="#fff" stroke-width="0.8" fill="none"/></svg>
          hello@brindlemail.com
        </li>
      </ul>
    </div>

    <div class="social" aria-label="Social profiles">
      <span></span><span></span><span></span>
    </div>
    <p class="address">1180 West Harbor Lane Tempe, AZ 85281</p>
  </section>

  <section class="card card--back" aria-label="Card back">
    <div class="brand">
      <span class="brand__mark"></span>
      <span class="brand__name">Brindle Advisory</span>
    </div>
    <span class="brand__tagline">business consulting</span>
    <p class="website">www.brindleadvisory.com</p>
  </section>
</body>
</html>
```